Business Card Design Project

Looking to update our business cards. We have a logo with our slogan. We are an IT firm so we wouldlike a modern look.

Industry/Entity Type

Business

```html
<!DOCTYPE html>
<html lang="en">
<head>
<meta charset="utf-8">
<title>Kernelo – Business Cards</title>
<link rel="stylesheet" href="https://fonts.googleapis.com/css2?family=Jost:wght@400;500&family=Arimo:wght@400;700&display=swap">
<style>
  :root {
    --bg: #ecebe8;
    --card: #ffffff;
    --green: #6b7f3e;
    --green-light: #9fbd3a;
    --ink: #2f2f2f;
    --divider: #c9c9c9;
  }
  * { box-sizing: border-box; margin: 0; padding: 0; }
  html, body { width: 1200px; height: 695px; overflow: hidden; }
  body {
    background: var(--bg);
    font-family: "Jost", "Futura", sans-serif;
    color: var(--ink);
    position: relative;
  }
  .card {
    position: absolute;
    top: 198px;
    width: 520px;
    height: 298px;
    background: var(--card);
    box-shadow: 0 6px 18px rgba(0,0,0,0.18);
    overflow: hidden;
  }
  .card--front { left: 50px; }
  .card--back { left: 630px; }

  /* front */
  .name-band {
    position: absolute;
    left: 0; right: 0; top: 42px;
    height: 46px;
    background: var(--green);
    display: flex; align-items: center; justify-content: center;
    color: #fff;
    font-family: "Arimo", Arial, sans-serif;
  }
  .name-band::before, .name-band::after {
    content: ""; position: absolute; left: 0; right: 0;
    height: 1px; background: var(--green-light);
  }
  .name-band::before { top: -7px; }
  .name-band::after { bottom: -7px; }
  .name-band__name { font-weight: 700; font-size: 20px; }
  .name-band__title { font-size: 13px; margin-left: 3px; }

  .brand {
    position: absolute;
    text-align: center;
    font-family: "Jost", sans-serif;
    font-weight: 500;
    color: var(--green);
    letter-spacing: 0.12em;
    text-transform: uppercase;
  }
  .card--front .brand { left: 30px; top: 172px; width: 290px; font-size: 38px; }
  .card--back .brand { left: 0; right: 0; top: 92px; font-size: 64px; }

  .divider {
    position: absolute; left: 330px; top: 120px;
    width: 1px; height: 150px; background: var(--divider);
  }
  .contact {
    position: absolute; left: 345px; top: 122px;
    list-style: none; font-size: 13px; line-height: 20px;
  }
  .contact li { display: flex; align-items: flex-start; gap: 6px; }
  .contact svg { width: 11px; height: 11px; margin-top: 4px; fill: var(--green); flex: none; }
  .contact .contact__address { margin-top: 12px; line-height: 16px; }

  /* back */
  .web {
    position: absolute; left: 0; right: 0; top: 218px;
    text-align: center; font-size: 26px; font-weight: 500;
    letter-spacing: 0.16em; color: var(--ink);
  }
</style>
</head>
<body>
  <section class="card card--front">
    <div class="name-band">
      <span class="name-band__name">Your Name,</span><span class="name-band__title">Title</span>
    </div>
    <p class="brand">Kernelo</p>
    <div class="divider"></div>
    <ul class="contact">
      <li><svg viewBox="0 0 12 12"><path d="M2 1h3l1 3-2 1a7 7 0 0 0 3 3l1-2 3 1v3c-6 0-10-4-10-10z"/></svg>0987 654321</li>
      <li><svg viewBox="0 0 12 12"><rect x="3" y="0.5" width="6" height="11" rx="1"/></svg>0987 654321</li>
      <li><svg viewBox="0 0 12 12"><path d="M1 2.5h10v7H1z M1 2.5l5 4 5-4" fill="none" stroke="#6b7f3e" stroke-width="1.3"/></svg>info@kernelo.com</li>
      <li><svg viewBox="0 0 12 12"><circle cx="6" cy="6" r="5" fill="none" stroke="#6b7f3e" stroke-width="1.2"/><path d="M1 6h10M6 1c-3 3-3 7 0 10M6 1c3 3 3 7 0 10" fill="none" stroke="#6b7f3e"/></svg>www.kernelo.com</li>
      <li class="contact__address"><svg viewBox="0 0 12 12"><path d="M6 0.5a4 4 0 0 0-4 4c0 3 4 7 4 7s4-4 4-7a4 4 0 0 0-4-4zm0 2.5a1.5 1.5 0 1 1 0 3 1.5 1.5 0 0 1 0-3z"/></svg><span>00, Complex name<br>City, State 0042</span></li>
    </ul>
  </section>

  <section class="card card--back">
    <p class="brand">Kernelo</p>
    <p class="web">www.kernelo.com</p>
  </section>
</body>
</html>
```